Electrical company business card design.

Hi, were an electrical company in Eastmere New Zealand called Quarneth Ltd. We focus mainly on high end residential and commercial so the card would be targeted towards that.
The card will be for myself, i am the director of the company.
Name: Derek Olstow
Position: Director/electrician
Phone: 021 387 9415
Email: derek@quarneth.co.nz
Location: Eastmere
As for colors the the blue color in the logo is preferred, i also don't mind a black background option.
Target Market(s)
High end residential and commercial
Industry/Entity Type
Electrician
Contact Information for Business Card
Name: Derek Olstow Position: Director/Electrician Phone: 021 387 9415, Email: derek@quarneth.co.nz, Location: Eastmere

```html
<!DOCTYPE html>
<html lang="en">
<head>
<meta charset="utf-8">
<title>Quarneth Ltd — Business Card</title>
<link rel="stylesheet" href="https://fonts.googleapis.com/css2?family=Montserrat:wght@600;700&family=Arimo:wght@400;700&display=swap">
<style>
  :root {
    --page-bg: #2b2b2e;
    --navy-deep: #03033a;
    --navy: #0d1660;
    --royal: #1f3a94;
    --sky: #2a9fd6;
    --accent: #2b8fd8;
    --white: #ffffff;
    --text-soft: #e8ecf7;
  }
  * { box-sizing: border-box; margin: 0; padding: 0; }
  html, body {
    width: 1200px;
    height: 900px;
    overflow: hidden;
    background: var(--page-bg);
  }
  .sheet {
    position: relative;
    width: 1200px;
    height: 900px;
    display: flex;
    flex-direction: column;
    align-items: center;
    justify-content: center;
    gap: 34px;
  }
  .card {
    position: relative;
    width: 700px;
    height: 400px;
    overflow: hidden;
    box-shadow: 0 14px 30px rgba(0,0,0,0.45);
  }

  /* Front */
  .card--front {
    border-radius: 40px 4px 40px 4px;
    background: linear-gradient(115deg, var(--sky) 0%, var(--royal) 38%, var(--navy) 72%, var(--navy-deep) 100%);
  }
  .card--front .brand {
    position: absolute;
    right: 60px;
    top: 150px;
    text-align: center;
  }

  /* Back */
  .card--back {
    border-radius: 4px 40px 4px 40px;
    background: var(--navy-deep);
  }

  .brand__name {
    font-family: "Montserrat", sans-serif;
    font-weight: 600;
    color: var(--white);
    letter-spacing: 4px;
    line-height: 1;
  }
  .brand__tagline {
    font-family: "Montserrat", sans-serif;
    font-weight: 700;
    color: var(--white);
    letter-spacing: 2.5px;
    text-transform: uppercase;
    white-space: nowrap;
  }
  .card--front .brand__name { font-size: 66px; }
  .card--front .brand__tagline { font-size: 17px; margin-top: 10px; }

  .contact {
    position: absolute;
    left: 52px;
    top: 54px;
    font-family: "Arimo", sans-serif;
    color: var(--text-soft);
  }
  .contact__name {
    font-weight: 700;
    font-size: 20px;
    letter-spacing: 0.5px;
    color: var(--accent);
    text-transform: uppercase;
  }
  .contact__role {
    font-size: 17px;
    margin-top: 4px;
  }
  .contact__list {
    list-style: none;
    margin-top: 12px;
  }
  .contact__item {
    display: flex;
    align-items: center;
    gap: 10px;
    font-size: 17px;
    margin-top: 6px;
  }
  .contact__icon {
    width: 16px;
    height: 16px;
    flex: none;
  }

  .card--back .brand {
    position: absolute;
    right: 50px;
    bottom: 70px;
    display: flex;
    align-items: center;
    gap: 16px;
  }
  .brand__mark {
    width: 22px;
    height: 22px;
    background: var(--accent);
    flex: none;
  }
  .card--back .brand__text { text-align: center; }
  .card--back .brand__name { font-size: 52px; }
  .card--back .brand__tagline { font-size: 13.5px; margin-top: 8px; }
</style>
</head>
<body>
  <main class="sheet">
    <section class="card card--front" aria-label="Card front">
      <div class="brand">
        <p class="brand__name">QUARNETH</p>
        <p class="brand__tagline">Current done carefully</p>
      </div>
    </section>

    <section class="card card--back" aria-label="Card back">
      <div class="contact">
        <p class="contact__name">Derek Olstow</p>
        <p class="contact__role">Director/Electrician</p>
        <ul class="contact__list">
          <li class="contact__item">
            <svg class="contact__icon" viewBox="0 0 24 24" aria-hidden="true">
              <path fill="#2b8fd8" d="M6.6 10.8a15.1 15.1 0 0 0 6.6 6.6l2.2-2.2a1 1 0 0 1 1-.25 11.4 11.4 0 0 0 3.6.57 1 1 0 0 1 1 1V20a1 1 0 0 1-1 1A17 17 0 0 1 3 4a1 1 0 0 1 1-1h3.5a1 1 0 0 1 1 1c0 1.25.2 2.45.57 3.6a1 1 0 0 1-.25 1z"/>
            </svg>
            <span>021 387 9415</span>
          </li>
          <li class="contact__item">
            <svg class="contact__icon" viewBox="0 0 24 24" aria-hidden="true">
              <path fill="#2b8fd8" d="M12 2a7 7 0 0 0-7 7c0 5.2 7 13 7 13s7-7.8 7-13a7 7 0 0 0-7-7zm0 9.5A2.5 2.5 0 1 1 12 6.5a2.5 2.5 0 0 1 0 5z"/>
            </svg>
            <span>Eastmere</span>
          </li>
        </ul>
      </div>

      <div class="brand">
        <span class="brand__mark" aria-hidden="true"></span>
        <div class="brand__text">
          <p class="brand__name">QUARNETH</p>
          <p class="brand__tagline">Current done carefully</p>
        </div>
      </div>
    </section>
  </main>
</body>
</html>
```